Create an Event-Centric WordPress Website for NGO

1. Project Overview

- We represent "Zusammen für Brockelsdorf e.V.", a non-profit association. Our outdated website www.zfbev-beispiel.de shall get a proper replacement.

- The primary goal of our new site is to showcase and facilitate bookings for our cultural events, including concerts, theme nights, joint dinners and village festivals.

- Alongside event bookings, we plan to introduce the public to our history, values, leadership team, and news through a regularly updated blog.

- At a later stage we aim to integrate a user-friendly web shop based on WooCommerce, offering a range of up to 10 products related to our organization. This web-shop is not part of this project! The only relevant item is to include one menu item called "Shop" in the menu bar within the header.

2. Design Requirements

- The design should lean towards a sleek, welcoming, and slightly playful OnePage layout for the main page with additional pages as required.

- The color scheme should integrate the blue and red from our logo, as detailed in the attached brand board. However, deviations that enhance the design are welcome.

- Essential files like logos, photos, and texts are provided in the attachments.

- Emphasis should be on illustrating the community spirit, our events, and the emotions they evoke.

- Mobile first! Of course we like a great design both on desktops and smartphones. Nevertheless, if priorizaztion is needed, mobiles comes first.

3. Site Structure and Navigation

The website should be structured as follows:

**Main Page:**
- Opening with a Gallery/Video/Slogan.
- Upcoming Events.
- Counters to track event attendance or other metrics.
- Shoet description of what we do incl. mission Statements.
- Team Introduction.
- Top News Highlights.
- Contact Form.

**Additional Pages:**
- **About Us:** Detailing our history, a gallery, and a membership form.
- **Shop:** The content and setup is not part of this project and shall only be displayed as a menu item in the upper menu bar in the header.
- **Data Protection & Imprint:** Accessible via footer links.

Social media buttons for Facebook and Instagram should be prominently placed, preferably in the footer.

I am not really sure, if the design contest includes one page only. For the project please concentrate anyhow on the main page and we can then clarify further details.

4. Technical Requirements

- The site is to be fully developed in WordPress.

- Samples for initial design, including products, news, and events, are attached. However, the end design should accommodate easy edits and content additions. For the news the blog function within WordPress shall be used.

- Usability is paramount. Therefore, the Elementor plugin should be incorporated for easy edits without in-depth technical knowledge.

5. Event Management

- Events should have categories (e.g., concerts, dinner parties).

- Direct ticket booking with a cap on maximum participants is a must. Potential tools include the WordPress plugin GatherDesk or wordpress themes like Vorelt. This project only includes the design of the elements related to the event booking on the main page. The setup of the e-commerce functionality Inch. payment, etc. is not part of this project and will be sourced separately at a later stage.

6. Responsiveness & Speed

- The site must be mobile-responsive, ensuring a seamless experience across devices.

- Page load speed is crucial. Optimizations should be made to ensure swift page loads.

7. SEO & Optimization

- The website should be built with basic SEO principles in mind, ensuring improved visibility on search engines.

8. Post-Design

- Upon design completion, a subsequent project will cover the WordPress setup on our KARVO hosting platform and content addition.

- Continuous direct feedback will be provided throughout the design process to ensure clarity and minimize revisions.

- Post handover, we will manage the site in-house. No long-term maintenance is required from the designer.

9. Additional Notes

- We're open to design deviations if they lead to enhanced outcomes or usability.

10. Sample texts

Main Page:

Opening (Slogan)
[EN]: Slogan for the main opening.
[DE]: "Nachbarschaft spüren. In Brockelsdorf daheim!"
Upcoming Events (Event Descriptions)
2.1 Mara Quell
[EN]: Description for Mara Quell's event.
[DE]: "Mara kehrt zurück! Am 10.11.2023 erneut in der Holunderscheune. Lassen Sie sich von ihrem Mix aus Schlagern und Evergreens mitreißen."
2.2 Spanischer Abend
[EN]: Description for the Italian evening.
[DE]: "La Dolce Vita in Brockelsdorf. Am 21.11.2023 genießen wir in der Holunderscheune authentische italienische Spezialitäten in einer warmen Atmosphäre."
Metrics (Counters)
[EN]: Counters to showcase community metrics.
[DE]:
Mitglieder: "XXX stolze Mitglieder."
Events in 2023: "XXX Events bisher in diesem Jahr."
Besucher: "XXX glückliche Besucher bei unseren Veranstaltungen."
Short Description (Values and Mission)
[EN]: Short descriptions for the community values.
[DE]:
Miteinander in Brockelsdorf stärken: "Unsere Gemeinschaft ist unser Herzstück. Wir setzen uns dafür ein, dass jeder Einwohner in Brockelsdorf sich zugehörig und geschätzt fühlt."
Kulturelles Angebot schaffen: "Kultur belebt! Durch Veranstaltungen, Konzerte und Feste bereichern wir das kulturelle Leben in Brockelsdorf."
Füreinander da sein: "In guten wie in schlechten Zeiten – wir stehen zusammen. Egal ob jung oder alt, jeder wird in unserer Gemeinschaft unterstützt."
Team (Board Members)
[EN]: Introduction of the board members with photos and titles.
[DE]: "Unser engagiertes Team. Lernen Sie die Köpfe hinter 'Zusammen für Brockelsdorf e.V.' kennen."
News (Recent News Highlights)
[EN]: Short description of a recent news event.
[DE]: Sommerfest in Brockelsdorf: "Ein voller Erfolg! Mit über 400 Besuchern feierten wir am 21.06.2023 unser traditionelles Sommerfest inklusive Vogelschießen."
Contact Form (Contact Details)
[EN]: Contact form header and description.
[DE]: "Wir sind für Sie da! Haben Sie Fragen, Anregungen oder möchten Sie uns unterstützen? Kontaktieren Sie uns – wir freuen uns auf Ihre Nachricht."

Target Market(s)

Our target audience are the approx. 2.150 citizens of our village based in Germany, east of Hamburg. Many families with children, but also elderly people a singles. Also, foreigners, who are specially interested in our events are considered as our target audience.

Industry/Entity Type

NGO (cultural events for local village community)

Coding

Coded - Design and coding required

Font styles to use
Sans Serif
Other font styles liked:
• We like the combination of OSWALD REGULAR for headlines and MONTSERRAT EXTRA LIGHT or LIGHT for plain text. Deviations which will support a better design are very much welcome.

Colors
0094D4
00A9DD
6FCCEA
C7EBF8
E9F6FB
EB3D1F
EC4F4E
F09395
F8D3D4
FCEDEE

Requirements
Must have
• The design must be adaptable to an event booking function. This can be either achieved by a WordPress plugin such an Event calendar or an Event Wordpress theme (Vorelt is preferred). The design shall but mobile first.
Nice to have
• Create an emotional, welcoming atmosphere. More human than streamlining.
Should not have
• We don't like a cold, too straight or too structured design.

```html
<!DOCTYPE html>
<html lang="de">
<head>
<meta charset="utf-8">
<title>Zusammen für Brockelsdorf e.V.</title>
<link rel="stylesheet" href="https://fonts.googleapis.com/css2?family=Oswald:wght@400;500&family=Montserrat:wght@300;400&display=swap">
<style>
:root{
  --blue:#1d3f98;
  --blue-deep:#16307c;
  --red:#e01f2f;
  --white:#ffffff;
  --text:#4a4a4a;
  --light:#e9edf5;
  --pink:#fbe6e7;
}
*{margin:0;padding:0;box-sizing:border-box}
html,body{width:1200px;height:5190px;overflow:hidden}
body{position:relative;background:var(--white);font-family:'Montserrat',sans-serif;font-weight:300;color:var(--text)}
.h{font-family:'Oswald',sans-serif;font-weight:400;text-transform:uppercase}
.abs{position:absolute}
.blue{color:var(--blue)}.red{color:var(--red)}
.mark{background:var(--red);color:#fff;padding:0 2px}

.topbar{left:0;top:0;width:1200px;height:9px;background:var(--red)}
.header{left:0;top:9px;width:1200px;height:100px;background:#fff}
.nav{top:46px;font-family:'Oswald',sans-serif;font-size:17px;color:#555;text-transform:uppercase;display:flex;gap:40px}
.brand{left:480px;top:9px;width:240px;height:132px;background:#fff;border-radius:0 0 120px 120px;z-index:3;display:flex;align-items:center;justify-content:center;gap:8px}
.brand-dot{width:12px;height:12px;border-radius:50%;background:var(--red);flex:none}
.brand-name{font-family:'Oswald',sans-serif;font-size:15px;color:var(--blue);white-space:nowrap}

.hero{left:0;top:109px;width:1200px;height:634px;background:linear-gradient(100deg,#6f8a3e 0%,#8a5a3c 30%,#9a4e36 55%,#6e6a64 80%,#8c8f8a 100%)}
.slogan{left:634px;top:355px;font-size:44px;line-height:52px;color:#fff;white-space:nowrap}

.sec-title{width:1200px;text-align:center;font-size:44px}
.card{width:456px;height:414px;background:#fff;box-shadow:0 2px 12px rgba(0,0,0,.18)}
.card svg{display:block}
.card-title{text-align:center;font-size:25px;margin-top:-8px}
.card-text{text-align:center;font-size:14.5px;line-height:20px;padding:12px 44px 0;color:#555}

.band{left:0;top:1396px;width:1200px;height:488px;background:linear-gradient(115deg,#2145a8 0%,#1a3a94 40%,#2349ae 60%,#183689 100%)}
.stats{left:127px;top:1491px;width:947px;height:302px;background:var(--red);display:flex;justify-content:space-around;padding-top:38px;color:#fff;text-align:center}
.stat{width:260px}
.stat .h{font-size:25px;margin-top:12px}
.stat p{font-size:16px;line-height:20px;margin-top:4px}

.mission{left:127px;top:2040px;width:430px}
.mission h2{font-size:46px}
.mission h3{font-size:25px;margin-top:36px}
.mission p{font-size:15px;line-height:19px;margin-top:8px;color:#555}
.accent{background:var(--red)}
.photo{background:linear-gradient(160deg,#8fb3d9 0%,#a79a88 40%,#8e6f5b 75%,#b3a48e 100%)}

.team{left:0;top:2797px;width:1200px;height:407px;display:flex;gap:2px}
.member{flex:1;position:relative;background:linear-gradient(180deg,#8b6a52 0%,#4c4035 45%,#1f2a4e 100%)}
.member span{position:absolute;bottom:30px;width:100%;text-align:center;color:#fff;font-size:21px}
.arrow{width:40px;height:40px;border-radius:50%;background:#fff;box-shadow:0 1px 6px rgba(0,0,0,.3);display:flex;align-items:center;justify-content:center}

.news{left:0;top:3290px;width:1200px;height:710px;background:linear-gradient(120deg,#dfe4ee 0%,#eef1f7 45%,#e3e8f1 100%)}
.lead{width:1200px;text-align:center;font-size:20px;line-height:25px;color:#444}

.field{left:127px;width:387px;height:50px;border:1px solid #d4d4d4;background:#fff;font-size:14px;color:#888;padding:16px 13px}
.submit{left:248px;top:4585px;width:146px;height:46px;background:var(--red);color:#fff;font-size:17px;display:flex;align-items:center;justify-content:center}

.contact-clip{left:578px;top:4226px;width:622px;height:494px;overflow:hidden}
.contact-arc{position:absolute;left:0;top:0;width:1000px;height:494px;border-radius:50%;border-left:5px solid var(--red)}
.contact-photo{position:absolute;left:12px;top:5px;width:1000px;height:484px;border-radius:50%;background:linear-gradient(120deg,#9a6a52 0%,#6f5648 30%,#2a3558 50%,#9c9488 70%)}

.footer-copy{width:1200px;text-align:center;color:#fff;font-size:15px}
.social{width:34px;height:34px;background:var(--red);border-radius:4px}
</style>
</head>
<body>

<div class="abs topbar"></div>
<header class="abs header">
  <nav class="abs nav" style="left:226px"><span>Home</span><span>About us</span><span>Shop</span></nav>
  <nav class="abs nav" style="left:742px"><span>Events</span><span>News</span><span>Contact</span></nav>
</header>
<div class="abs brand"><span class="brand-dot"></span><span class="brand-name">Zusammen für Brockelsdorf e.V.</span></div>

<section class="abs hero" role="img" aria-label="Foto: Vereinsmitglied am Grill vor der Holunderscheune, Gäste im Hintergrund"></section>
<h1 class="abs h slogan">Nachbarschaft spüren.<br>In Brockelsdorf daheim!</h1>

<h2 class="abs h sec-title" style="top:800px"><span class="blue">Upcoming</span> <span class="red">Events</span></h2>

<article class="abs card" style="left:127px;top:888px">
  <svg width="456" height="290" role="img" aria-label="Foto: Menschenmenge bei einem Fest im Freien">
    <defs><linearGradient id="e1" x1="0" y1="0" x2="0" y2="1"><stop offset="0" stop-color="#5d8fd6"/><stop offset=".5" stop-color="#6f7a58"/><stop offset="1" stop-color="#3b3f46"/></linearGradient></defs>
    <rect width="456" height="290" fill="url(#e1)"/>
    <path d="M0 290 L0 280 Q228 180 456 280 L456 290Z" fill="#fff"/>
  </svg>
  <h3 class="h card-title blue">Mara Quell</h3>
  <p class="card-text">Mara kehrt zurück! Am <span class="mark">10.11.2023</span> erneut in der Holunderscheune. Lassen Sie sich von ihrem Mix aus Schlagern und Evergreens mitreißen.</p>
</article>

<article class="abs card" style="left:618px;top:888px">
  <svg width="456" height="290" role="img" aria-label="Foto: Gäste an gedeckten Tischen beim Abendessen">
    <defs><linearGradient id="e2" x1="0" y1="0" x2="1" y2="1"><stop offset="0" stop-color="#6e5240"/><stop offset=".5" stop-color="#3d2e27"/><stop offset="1" stop-color="#8a6a52"/></linearGradient></defs>
    <rect width="456" height="290" fill="url(#e2)"/>
    <path d="M0 290 L0 280 Q228 180 456 280 L456 290Z" fill="#fff"/>
  </svg>
  <h3 class="h card-title red">Spanischer Abend</h3>
  <p class="card-text">La Dolce Vita in Brockelsdorf. Am <span class="mark">21.11.2023</span> genießen wir in der Holunderscheune authentische italienische Spezialitäten in einer warmen Atmosphäre.</p>
</article>

<section class="abs band"></section>
<section class="abs stats">
  <div class="stat">
    <svg width="90" height="90" viewBox="0 0 64 64" fill="none" stroke="#fff" stroke-width="2"><path d="M32 4l2 5 5 .5-4 3.5 1.5 5-4.5-3-4.5 3 1.5-5-4-3.5 5-.5z"/><circle cx="32" cy="30" r="6"/><circle cx="14" cy="36" r="6"/><circle cx="50" cy="36" r="6"/><path d="M22 58v-8a10 10 0 0120 0v8M3 60v-6a11 11 0 0122 0M39 54a11 11 0 0122 0v6"/></svg>
    <div class="h">Mitglieder</div><p>XXX stolze Mitglieder.</p>
  </div>
  <div class="stat">
    <svg width="90" height="90" viewBox="0 0 64 64" fill="none" stroke="#fff" stroke-width="2"><rect x="5" y="10" width="54" height="50" rx="3"/><path d="M5 22h54M18 4v12M46 4v12"/><path d="M32 28l3.5 7 7.5 1-5.5 5 1.5 7.5-7-4-7 4 1.5-7.5-5.5-5 7.5-1z"/></svg>
    <div class="h">Events in 2023</div><p>XXX Events bisher in<br>diesem Jahr.</p>
  </div>
  <div class="stat">
    <svg width="90" height="90" viewBox="0 0 64 64" fill="none" stroke="#fff" stroke-width="2"><path d="M32 30s-9-9-9-15a9 9 0 0118 0c0 6-9 15-9 15z"/><circle cx="32" cy="15" r="3"/><circle cx="12" cy="40" r="5"/><circle cx="32" cy="40" r="5"/><circle cx="52" cy="40" r="5"/><path d="M3 60a9 9 0 0118 0M23 60a9 9 0 0118 0M43 60a9 9 0 0118 0"/></svg>
    <div class="h">Besucher</div><p>XXX glückliche<br>Besucher bei unseren<br>Veranstaltungen.</p>
  </div>
</section>

<section class="abs mission">
  <h2 class="h blue">Werte und Mission</h2>
  <h3 class="h"><span class="red">Miteinander</span> <span class="blue">in Brockelsdorf stärken:</span></h3>
  <p>Unsere Gemeinschaft ist unser Herzstück. Wir setzen uns dafür ein, dass jeder Einwohner in Brockelsdorf sich zugehörig und geschätzt fühlt.</p>
  <h3 class="h"><span class="red">Kulturelles</span> <span class="blue">Angebot schaffen:</span></h3>
  <p>Kultur belebt! Durch Veranstaltungen, Konzerte und Feste bereichern wir das kulturelle Leben in Brockelsdorf.</p>
  <h3 class="h"><span class="red">Füreinander</span> <span class="blue">da sein:</span></h3>
  <p>In guten wie in schlechten Zeiten – wir stehen zusammen. Egal ob jung oder alt, jeder wird in unserer Gemeinschaft unterstützt.</p>
</section>
<div class="abs accent" style="left:1060px;top:2068px;width:26px;height:238px"></div>
<div class="abs accent" style="left:596px;top:2306px;width:74px;height:237px"></div>
<div class="abs photo" style="left:616px;top:2000px;width:458px;height:529px" role="img" aria-label="Foto: Besucher sitzen beim Dorffest auf dem Platz vor Zelten"></div>

<h2 class="abs h sec-title" style="top:2660px"><span class="blue">Unser</span> <span class="red">engagiertes</span> <span class="blue">Team</span></h2>
<p class="abs lead" style="top:2732px">Lernen Sie die Köpfe hinter 'Zusammen für Brockelsdorf e.V.' kennen.</p>
<section class="abs team">
  <div class="member" role="img" aria-label="Porträtfoto Vorstandsmitglied"><span class="h">Ilka Brandtner</span></div>
  <div class="member" role="img" aria-label="Porträtfoto Vorstandsmitglied"><span class="h">Sabine Wohlert</span></div>
  <div class="member" role="img" aria-label="Porträtfoto Vorstandsmitglied"><span class="h">Hans-Dieter Rehmkamp</span></div>
  <div class="member" role="img" aria-label="Porträtfoto Vorstandsmitglied"><span class="h">Jonas Treder</span></div>
</section>
<div class="abs arrow" style="left:-8px;top:2924px"><svg width="12" height="14"><path d="M9 2L3 7l6 5" fill="none" stroke="#222" stroke-width="2"/></svg></div>
<div class="abs arrow" style="left:1164px;top:2924px"><svg width="12" height="14"><path d="M3 2l6 5-6 5" fill="none" stroke="#222" stroke-width="2"/></svg></div>

<section class="abs news"></section>
<h2 class="abs h sec-title" style="top:3366px"><span class="blue">Sommerfest in</span> <span class="red">Brockelsdorf</span></h2>
<p class="abs lead" style="top:3434px">Ein voller Erfolg! Mit über 400 Besuchern feierten wir am <span class="mark">21.06.2023</span><br>unser traditionelles Sommerfest inklusive Vogelschießen.</p>
<div class="abs" style="left:254px;top:3522px;width:693px;height:391px;background:linear-gradient(120deg,#5a4a3e 0%,#2f2a28 40%,#6b5a4b 70%,#3f4a5a 100%)" role="img" aria-label="Foto: Gäste am festlich gedeckten Tisch beim Sommerfest"></div>
<div class="abs arrow" style="left:234px;top:3697px"><svg width="12" height="14"><path d="M9 2L3 7l6 5" fill="none" stroke="#222" stroke-width="2"/></svg></div>
<div class="abs arrow" style="left:927px;top:3697px"><svg width="12" height="14"><path d="M3 2l6 5-6 5" fill="none" stroke="#222" stroke-width="2"/></svg></div>

<div class="abs" style="left:-260px;top:4050px;width:540px;height:540px;border-radius:50%;background:var(--pink)"></div>
<h2 class="abs h sec-title" style="top:4068px"><span class="blue">Kontaktiere</span> <span class="red">uns</span></h2>
<p class="abs lead" style="top:4148px">Wir sind für Sie da! Haben Sie Fragen, Anregungen oder möchten Sie uns<br>unterstützen? Kontaktieren Sie uns – wir freuen uns auf Ihre Nachricht.</p>
<form>
  <div class="abs field" style="top:4288px">Name:</div>
  <div class="abs field" style="top:4352px">Email:</div>
  <div class="abs field" style="top:4416px">Phone:</div>
  <div class="abs field" style="top:4482px;height:130px">Message:</div>
  <div class="abs h submit">Submit now</div>
</form>
<div class="abs contact-clip">
  <div class="contact-arc"></div>
  <div class="contact-photo" role="img" aria-label="Foto: Vorstandsmitglieder im Gespräch am Holztisch vor der Scheune"></div>
</div>

<footer>
  <svg class="abs" style="left:0;top:4755px" width="1200" height="435" viewBox="0 0 1200 435">
    <path d="M0 0 Q600 95 1200 0 L1200 435 L0 435Z" fill="var(--blue)"/>
    <path d="M110 60 Q600 135 1090 58" fill="none" stroke="var(--red)" stroke-width="4"/>
  </svg>
  <div class="abs" style="left:450px;top:4886px;width:300px;height:112px;display:flex;align-items:center;justify-content:center;gap:8px">
    <span class="brand-dot"></span><span class="brand-name" style="color:#fff">Zusammen für Brockelsdorf e.V.</span>
  </div>
  <p class="abs footer-copy" style="top:5032px">© 2023 All rights are reserved. Data Protection &amp; Imprint</p>
  <div class="abs social" style="left:560px;top:5070px" aria-label="Soziales Netzwerk"></div>
  <div class="abs social" style="left:606px;top:5070px" aria-label="Soziales Netzwerk"></div>
</footer>

</body>
</html>
```